Hartwell's Roving Meats, needs a Business card design that stands out from the crowd

We need a business card design for our mobile butchering business. We are a small business that wants to increase our customer base. Convenient, reliable, hygienic and quality service. We would like our logo as a key component of our card and to incorporate some colours and patterns to blend with it and stand out, making it appealing to the eye of potential customers. We would like it to look somewhat professional. On the back we would like our logo as the stand out, ensuring that out business name is on there and also the Quality Service-Quality Price slogan.

Target Market(s)

Farmers

Industry/Entity Type

Business

Contact Information for Business Card

Information we would like on the card, including;' Ray Dunmore' on the card. email: 'rayandtess@quillmail.example address': '7 Brampton Rd, Ooralea QLD 4740'. phone numbers; 'Ray#0412657381' or 'Tess#0417320946'. Like us on facebook, 'Hartwell's Roving Meats'

Font styles to use
Serif

Colors
ec1f27
3176b5
85cae6
cfdfed
0255a3

Requirements
Must have
• Our Business logo and all the information in card details.
• Our business logo on both sides. the side that doesn't have the details on it, needs to have our logo as the stand out and ensure our business name and slogan 'Quality Service-Quality Price' is on there.
• Ray Dunmore needs to be on the card details side also.
Nice to have
• Incorporated shapes, designs, colours to blend and make stand out
Should not have
• Oranges or colours that are too dark, including just black. Black can be incorporated to enhance the look. However we do not like all black cards, thank you

```html
<!DOCTYPE html>
<html lang="en">
<head>
<meta charset="utf-8">
<title>Hartwell's Roving Meats – Business Card</title>
<link href="https://fonts.googleapis.com/css2?family=Open+Sans:wght@400;600&display=swap" rel="stylesheet">
<style>
  :root {
    --page: #e8e4de;
    --red: #ec1f27;
    --red-deep: #c8141b;
    --red-light: #f2474e;
    --black: #121315;
    --black-soft: #26282c;
    --rim: #6f8fb8;
    --steel: #6c86ab;
    --grey: #6d6f73;
    --white: #ffffff;
  }
  * { box-sizing: border-box; margin: 0; padding: 0; }
  html, body { width: 1200px; height: 1023px; overflow: hidden; }
  body {
    background: var(--page);
    font-family: "Open Sans", sans-serif;
    position: relative;
  }
  .card {
    position: absolute;
    width: 540px;
    height: 310px;
    border-radius: 20px;
    overflow: hidden;
    box-shadow: 0 10px 24px rgba(0,0,0,.22);
  }
  .card--details {
    left: 45px; top: 356px;
    background: linear-gradient(160deg, var(--black-soft), var(--black) 60%);
  }
  .card--brand {
    left: 615px; top: 356px;
    background: linear-gradient(150deg, var(--red-light), var(--red) 45%, var(--red-deep));
  }
  .card__shape { position: absolute; inset: 0; }

  .logo-art {
    position: absolute;
    border-radius: 50%;
    background: radial-gradient(circle at 45% 45%, #8a8c90, var(--grey) 45%, var(--steel) 75%, rgba(108,134,171,0) 76%);
  }
  .card--details .logo-art { width: 140px; height: 140px; left: 385px; top: 34px; }
  .card--brand .logo-art { width: 190px; height: 190px; left: 175px; top: 60px; }

  .brand-name {
    position: absolute;
    color: var(--white);
    font-weight: 400;
    white-space: nowrap;
    display: flex;
    align-items: center;
    gap: 7px;
  }
  .brand-name::before {
    content: "";
    width: 9px; height: 9px;
    border-radius: 50%;
    background: var(--white);
  }
  .card--details .brand-name { font-size: 13px; right: 22px; top: 12px; }
  .card--brand .brand-name { font-size: 21px; left: 150px; top: 22px; }

  .slogan {
    position: absolute;
    color: var(--white);
    white-space: nowrap;
  }
  .card--details .slogan { font-size: 12px; right: 16px; top: 182px; }
  .card--brand .slogan { font-size: 17px; left: 0; right: 0; text-align: center; top: 266px; }

  .person { position: absolute; left: 36px; top: 118px; color: var(--red); line-height: 1.05; }
  .person__name { font-size: 30px; font-weight: 400; }
  .person__role { font-size: 19px; margin-top: 2px; }

  .contacts {
    position: absolute;
    left: 120px; top: 208px;
    list-style: none;
    color: var(--white);
    font-size: 14px;
    line-height: 22px;
  }
  .contacts li { display: flex; align-items: center; gap: 10px; }
  .contacts .icon {
    width: 16px; height: 16px;
    border-radius: 3px;
    background: var(--red);
    flex: none;
  }
  .contacts .icon svg { display: block; width: 16px; height: 16px; }
</style>
</head>
<body>

<section class="card card--details" aria-label="Business card, details side">
  <svg class="card__shape" viewBox="0 0 540 310" aria-hidden="true">
    <circle cx="470" cy="40" r="213" fill="var(--rim)"/>
    <circle cx="470" cy="40" r="208" fill="var(--red)"/>
  </svg>
  <p class="brand-name">Hartwell's Roving Meats</p>
  <div class="logo-art" role="img" aria-label="Brand illustration: bull head with crossed cleavers"></div>
  <p class="slogan">Quality Service-Quality Price</p>

  <div class="person">
    <p class="person__name">Ray Dunmore</p>
    <p class="person__role">Butcher</p>
  </div>

  <ul class="contacts">
    <li><span class="icon"><svg viewBox="0 0 16 16"><path d="M5 3.5 L6.8 5.8 L5.8 7 Q7 9.4 9 10.2 L10.2 9.2 L12.5 11 L11.4 12.6 Q6.5 12 3.6 5 Z" fill="#fff"/></svg></span>+61 412 657 381 (Ray)</li>
    <li><span class="icon"><svg viewBox="0 0 16 16"><path d="M5 3.5 L6.8 5.8 L5.8 7 Q7 9.4 9 10.2 L10.2 9.2 L12.5 11 L11.4 12.6 Q6.5 12 3.6 5 Z" fill="#fff"/></svg></span>+0438204715 (Tess)</li>
    <li><span class="icon"><svg viewBox="0 0 16 16"><rect x="3" y="4.5" width="10" height="7" fill="none" stroke="#fff" stroke-width="1.3"/><path d="M3 4.5 L8 9 L13 4.5" fill="none" stroke="#fff" stroke-width="1.3"/></svg></span>rayandtess@quillmail.example</li>
    <li><span class="icon"></span>Hartwell's Roving Meats</li>
  </ul>
</section>

<section class="card card--brand" aria-label="Business card, brand side">
  <p class="brand-name">Hartwell's Roving Meats</p>
  <div class="logo-art" role="img" aria-label="Brand illustration: bull head with crossed cleavers"></div>
  <p class="slogan">Quality Service-Quality Price</p>
</section>

</body>
</html>
```